Halvex Therapeutics is a biotech company that needs a powerpoint theme.

We need a powerpoint theme with several different slide templates we could use for presentation of data or research ideas. Our logo is attached. We picked "Halvex" as our company name because we use epigenome editing tools to fine-tune gene expression for therapeutic purposes. Our logo color is a seafoam green, and we would like to see this color along with other colors that could complement it well. Keywords: genetics, biotech, cells, human therapies,

```html
<!DOCTYPE html>
<html lang="en">
<head>
<meta charset="utf-8">
<title>Halvex Therapeutics – Presentation Theme</title>
<link rel="stylesheet" href="https://fonts.googleapis.com/css2?family=Bebas+Neue&family=Lilita+One&display=swap">
<style>
  :root {
    --paper: #ffffff;
    --heading: #05957f;
    --seafoam: #0dbba6;
    --seafoam-light: #13c9b2;
    --seafoam-mid: #0aa893;
    --seafoam-text: #0aa090;
    --seafoam-glow: #1ee8cc;
    --deep: #037c6e;
    --deep-blob: #069684;
    --deep-text: #07907f;
    --logo-outer: #088f7e;
    --logo-inner: #0a7d6d;
    --logo-ink: #2e3433;
    --split-light: #0ab09c;
    --split-mid: #09a08d;
    --split-dark: #0a7e6c;
    --split-text: #20c9b0;
    --white: #ffffff;
    --photo-sky: #b6dcf2;
    --photo-sky-deep: #9cc6ea;
  }
  html, body {
    margin: 0;
    padding: 0;
    width: 1200px;
    height: 1200px;
    overflow: hidden;
    background: var(--paper);
  }
  .sheet {
    position: relative;
    width: 1200px;
    height: 1200px;
  }
  .sheet-heading {
    position: absolute;
    left: 0;
    width: 1200px;
    margin: 0;
    text-align: center;
    font-family: "Lilita One", sans-serif;
    font-weight: 400;
    font-size: 98px;
    line-height: 1;
    letter-spacing: 3px;
    color: var(--heading);
  }
  .sheet-heading--top { top: 120px; left: -6px; }
  .sheet-heading--bottom { top: 992px; left: 2px; }
  .slide {
    position: absolute;
    width: 482px;
    height: 300px;
    display: block;
  }
  .slide--cover { left: 108px; top: 314px; }
  .slide--gallery { left: 616px; top: 314px; }
  .slide--brand { left: 108px; top: 627px; }
  .slide--split { left: 616px; top: 627px; }
  .slide text {
    font-family: "Bebas Neue", sans-serif;
  }
  .brand-name {
    font-family: "Bebas Neue", sans-serif;
  }
</style>
</head>
<body>
<main class="sheet">
  <h1 class="sheet-heading sheet-heading--top">SAMPLE DESIGN</h1>

  <!-- Cover slide -->
  <svg class="slide slide--cover" viewBox="0 0 482 300" xmlns="http://www.w3.org/2000/svg">
    <rect width="482" height="300" fill="var(--seafoam)"/>
    <path d="M390,0 L482,0 L482,120 C462,72 430,30 390,0Z" fill="var(--seafoam-light)"/>
    <path d="M0,165 C30,218 80,232 180,240 C265,248 296,278 300,300 L0,300Z" fill="var(--seafoam-mid)"/>
    <path d="M395,300 C440,282 470,262 482,250 L482,300Z" fill="var(--seafoam-light)"/>
    <g fill="var(--seafoam-text)" font-size="28">
      <text x="200" y="116">TYPE HERE</text>
      <text x="200" y="138">TYPE HERE</text>
      <text x="200" y="161">TYPE HERE</text>
    </g>
    <text x="21" y="283" font-size="29" fill="var(--seafoam-glow)">TYPE HERE</text>
  </svg>

  <!-- Gallery slide -->
  <svg class="slide slide--gallery" viewBox="0 0 482 300" xmlns="http://www.w3.org/2000/svg">
    <rect width="482" height="300" fill="var(--deep)"/>
    <path d="M193,0 C202,22 198,60 230,76 C256,89 282,80 290,58 L294,242 C270,236 250,240 240,256 C230,272 232,294 205,300 L482,300 L482,0Z" fill="var(--deep-blob)"/>
    <g fill="var(--deep-text)" font-size="28">
      <text x="34" y="140">TYPE HERE</text>
      <text x="34" y="162">TYPE HERE</text>
      <text x="34" y="185">TYPE HERE</text>
    </g>
    <rect x="180" y="77" width="114" height="165" fill="var(--photo-sky)" role="img" aria-label="Photo: lab still life with petri dishes, syringe, face mask and capsules"/>
    <rect x="312" y="21" width="154" height="246" fill="var(--photo-sky-deep)" role="img" aria-label="Photo: gloved hands holding a petri dish"/>
  </svg>

  <!-- Brand slide -->
  <svg class="slide slide--brand" viewBox="0 0 482 300" xmlns="http://www.w3.org/2000/svg">
    <rect width="482" height="300" fill="var(--logo-outer)"/>
    <path d="M0,70 C60,56 130,28 250,25 C350,24 420,40 482,52 L482,245 C440,284 405,300 390,300 L105,300 C60,284 22,262 0,240Z" fill="var(--logo-inner)"/>
    <circle cx="155" cy="143" r="36" fill="var(--seafoam)"/>
    <text class="brand-name" x="212" y="152" font-size="30" fill="var(--logo-ink)" letter-spacing="1">HALVEX THERAPEUTICS</text>
  </svg>

  <!-- Split content slide -->
  <svg class="slide slide--split" viewBox="0 0 482 300" xmlns="http://www.w3.org/2000/svg">
    <rect width="482" height="300" fill="var(--split-light)"/>
    <path d="M185,0 C172,60 98,140 98,165 C108,200 132,220 128,246 C114,280 40,290 0,300 L482,300 L482,0Z" fill="var(--split-mid)"/>
    <path d="M200,0 C185,52 108,130 108,156 C118,186 136,202 140,232 C140,270 72,292 40,300 L482,300 L482,0Z" fill="var(--split-dark)"/>
    <text x="19" y="49" font-size="26" fill="var(--white)">TITLE HERE</text>
    <text x="19" y="67" font-size="20" fill="var(--white)">TITLE HERE</text>
    <text x="200" y="151" font-size="28" fill="var(--split-text)">TYPE HERE TYPE HERE</text>
    <text x="200" y="165" font-size="17" fill="var(--split-text)">TYPE HERE TYPE HERE</text>
  </svg>

  <h2 class="sheet-heading sheet-heading--bottom">SAMPLE DESIGN</h2>
</main>
</body>
</html>
```